Custom Die cut yard sign

Hi!

I would love to get really eye catching creative here with some window cleaning die cut signs!

I would like the main words to stand out of just saying, "Window Cleaning"

My phone number: 612-555-0143
Website: BrindlewayMN.com

My logo but it can be small as I want the "Window Cleaning and Phone number to really pop.

It can be a creative for implying window cleaning! Die cut so maybe water? Light? Windows outlines, squeegee? I don't know it's for residential window cleaning!

Attached is my logo and the template for the die cut sign.

Thanks!

```html
<!DOCTYPE html>
<html lang="en">
<head>
<meta charset="utf-8">
<title>Brindleway Window Cleaning – Die Cut Yard Sign Options</title>
<link rel="stylesheet" href="https://fonts.googleapis.com/css2?family=Roboto+Condensed:wght@800&family=Lato:wght@400&display=swap">
<style>
  :root {
    --backdrop: #3a1f10;
    --headline-green: #9ccc2a;
    --headline-green-dark: #6f9a12;
    --band-blue: #1d5fa8;
    --band-blue-deep: #0f3f7d;
    --drop-blue: #1466c8;
    --drop-deep: #0a2f86;
    --drop-light: #4fd0f2;
    --water-light: #bfe6f7;
    --ink-white: #ffffff;
    --drop-yellow: #d8e826;
  }
  html, body {
    margin: 0;
    width: 888px;
    height: 1200px;
    overflow: hidden;
    background: var(--backdrop);
  }
  .board { display: block; width: 888px; height: 1200px; }
  .sign-type {
    font-family: "Roboto Condensed", "Arial Narrow", sans-serif;
    font-weight: 800;
  }
  .option-label {
    font-family: "Lato", Arial, sans-serif;
    font-size: 25px;
    fill: var(--ink-white);
    letter-spacing: 0.5px;
  }
  .headline { fill: var(--headline-green); }
  .contact { fill: var(--ink-white); }
  .drop-headline { fill: var(--drop-yellow); }
  .brand-name { fill: var(--ink-white); }
</style>
</head>
<body>
<svg class="board" width="888" height="1200" viewBox="0 0 888 1200" xmlns="http://www.w3.org/2000/svg">
  <defs>
    <linearGradient id="band-gradient" x1="0" y1="0" x2="1" y2="0">
      <stop offset="0" stop-color="var(--band-blue-deep)"/>
      <stop offset="0.5" stop-color="var(--band-blue)"/>
      <stop offset="1" stop-color="var(--band-blue-deep)"/>
    </linearGradient>
    <radialGradient id="splash-gradient" cx="0.55" cy="0.5" r="0.55">
      <stop offset="0" stop-color="#2f8fd6"/>
      <stop offset="0.55" stop-color="var(--water-light)"/>
      <stop offset="1" stop-color="#ffffff" stop-opacity="0"/>
    </radialGradient>
    <radialGradient id="drop-gradient" cx="0.5" cy="0.75" r="0.7">
      <stop offset="0" stop-color="var(--drop-light)"/>
      <stop offset="0.45" stop-color="var(--drop-blue)"/>
      <stop offset="1" stop-color="var(--drop-deep)"/>
    </radialGradient>
    <clipPath id="sign-one-clip">
      <rect x="158" y="122" width="566" height="424"/>
    </clipPath>
  </defs>

  <!-- Option 1: rectangular sign -->
  <g class="sign-rect" clip-path="url(#sign-one-clip)">
    <rect x="158" y="122" width="566" height="424" fill="#ffffff"/>
    <rect class="splash-area" x="440" y="130" width="300" height="320" fill="url(#splash-gradient)"
          role="img" aria-label="Photographic splash of clear blue water curling like a wave"/>
    <path d="M158 330 Q 420 280 724 418 V546 H158 Z" fill="var(--headline-green)"/>
    <path d="M158 346 Q 420 296 724 426 V546 H158 Z" fill="#ffffff"/>
    <path d="M158 356 Q 420 306 724 432 V546 H158 Z" fill="url(#band-gradient)"/>

    <text class="sign-type headline" x="178" y="215" font-size="74" textLength="252" lengthAdjust="spacingAndGlyphs">WINDOW</text>
    <text class="sign-type headline" x="190" y="303" font-size="74" textLength="276" lengthAdjust="spacingAndGlyphs">CLEANING</text>

    <g class="phone-icon">
      <rect x="172" y="430" width="22" height="22" rx="4" fill="var(--headline-green)"/>
      <path d="M178 434 q-2 2 0 7 q3 6 8 8 q4 1 5 -1 l-3 -3 l-2 1 q-3 -2 -4 -5 l1 -2 z" fill="var(--band-blue-deep)"/>
    </g>
    <text class="sign-type contact" x="208" y="457" font-size="42" textLength="236" lengthAdjust="spacingAndGlyphs">612-555-0143</text>

    <g class="globe-icon" fill="none" stroke="var(--headline-green)" stroke-width="2">
      <circle cx="183" cy="493" r="10"/>
      <ellipse cx="183" cy="493" rx="4.5" ry="10"/>
      <line x1="173" y1="493" x2="193" y2="493"/>
    </g>
    <text class="sign-type contact" x="208" y="508" font-size="42" textLength="266" lengthAdjust="spacingAndGlyphs">BrindlewayMN.com</text>

    <g class="brand-mark">
      <circle cx="652" cy="468" r="12" fill="var(--band-blue-deep)" stroke="#ffffff" stroke-width="2"/>
      <text class="sign-type brand-name" x="652" y="499" font-size="16" text-anchor="middle">BRINDLEWAY</text>
    </g>
  </g>
  <text class="option-label" x="444" y="599" text-anchor="middle">OPTION 1</text>

  <!-- Option 2: water drop die cut -->
  <g class="sign-drop">
    <path d="M443 652 C 466 760, 580 852, 580 950 A 137 140 0 0 1 304 950 C 304 852, 420 760, 443 652 Z"
          fill="url(#drop-gradient)" stroke="#0a2a70" stroke-width="2"/>
    <text class="sign-type drop-headline" x="383" y="845" font-size="31" textLength="118" lengthAdjust="spacingAndGlyphs">WINDOW</text>
    <text class="sign-type drop-headline" x="375" y="886" font-size="31" textLength="134" lengthAdjust="spacingAndGlyphs">CLEANING</text>
    <text class="sign-type contact" x="349" y="953" font-size="31" textLength="195" lengthAdjust="spacingAndGlyphs">612-555-0143</text>
    <text class="sign-type contact" x="333" y="995" font-size="31" textLength="219" lengthAdjust="spacingAndGlyphs">BrindlewayMN.com</text>
    <g class="brand-mark">
      <circle cx="443" cy="1025" r="11" fill="var(--drop-deep)" stroke="#ffffff" stroke-width="2"/>
      <text class="sign-type brand-name" x="443" y="1054" font-size="15" text-anchor="middle">BRINDLEWAY</text>
    </g>
  </g>
  <text class="option-label" x="444" y="1172" text-anchor="middle">OPTION 2</text>
</svg>
</body>
</html>
```